Offshore Energy Projects Management Consultancy needs a business card design

Logo available. We provide teams to deliver engineering consultancy, project management and delivery teams mainly in the offshore renewables sector. The company is all about bringing the right people to a project to deliver the scope.

The business card will be used for all staff.

The business card should be quite simple, vibrant and uncluttered but convey experience, enthusiasm and integration.

Target Market(s)

Energy Project Developers and Tier 1 construction companies

Contact Information for Business Card

Logo should be on the back of the card. I'm happy for the designer to play with the colour of the logo and background colour.

Front of the card should convey all the must have information in a clear and professional manner but without being overly traditional.

Colors

Designer to choose colors to be used in the design.

Requirements
Must have
• Land Line Tel Number, Mobile Tel Number, Email, business address, web address.

```html
<!DOCTYPE html>
<html lang="en">
<head>
<meta charset="utf-8">
<title>Seaward Delivery Group – Business Card</title>
<link href="https://fonts.googleapis.com/css2?family=Lato:wght@400;700&display=swap" rel="stylesheet">
<style>
  :root {
    --backdrop: #b9b9b9;
    --sky-blue: #24a7e0;
    --deep-blue: #1b75bb;
    --white: #ffffff;
    --ink-grey: #686868;
    --card-shadow: 0 3px 6px rgba(0,0,0,0.35);
  }
  * { box-sizing: border-box; margin: 0; padding: 0; }
  html, body {
    width: 1200px; height: 802px; overflow: hidden;
    background: var(--backdrop);
    font-family: "Lato", sans-serif;
  }
  .stage { position: relative; width: 1200px; height: 802px; }
  .card {
    position: absolute; top: 274px;
    width: 442px; height: 264px;
    box-shadow: var(--card-shadow);
    overflow: hidden;
  }
  .card-front { left: 136px; background: var(--sky-blue); color: var(--white); }
  .card-back { left: 624px; background: var(--white); }

  .front-panel {
    position: absolute; left: 0; top: 0;
    width: 190px; height: 264px;
    background: var(--deep-blue);
  }
  .front-details {
    position: absolute; right: 17px; top: 28px;
    text-align: right;
  }
  .person-name {
    font-weight: 700; font-size: 18px; letter-spacing: 0.2px;
    text-transform: uppercase; line-height: 1.1;
  }
  .person-role { font-size: 13px; line-height: 1.15; }
  .contact-list { list-style: none; margin-top: 42px; }
  .contact-list li {
    font-size: 13px; line-height: 16px; height: 16px;
    display: flex; justify-content: flex-end; align-items: center; gap: 3px;
  }
  .contact-list svg { width: 10px; height: 10px; fill: var(--white); flex: none; }
  .address { margin-top: 16px; font-size: 13px; line-height: 15.5px; }

  .brand {
    position: absolute; left: 0; right: 0; top: 116px;
    display: flex; justify-content: center; align-items: center; gap: 10px;
  }
  .brand-dot {
    width: 16px; height: 16px; border-radius: 50%;
    background: var(--deep-blue);
  }
  .brand-name {
    font-weight: 700; font-size: 24px; color: var(--ink-grey);
    text-transform: uppercase; letter-spacing: 0.5px;
  }
</style>
</head>
<body>
<div class="stage">
  <section class="card card-front">
    <div class="front-panel"></div>
    <div class="front-details">
      <h1 class="person-name">Jordan Ellis</h1>
      <p class="person-role">Managing Director</p>
      <ul class="contact-list">
        <li>044-163 296 0123
          <svg viewBox="0 0 10 10"><path d="M1 4 Q5 0 9 4 L8 5 L6.5 4.3 L6.5 3.4 Q5 3 3.5 3.4 L3.5 4.3 L2 5 Z M2.5 5.5 L7.5 5.5 L8.5 9 L1.5 9 Z"/></svg></li>
        <li>044-163 296 0456
          <svg viewBox="0 0 10 10"><path d="M2.5 0 H7.5 V10 H2.5 Z M3.4 1 V8 H6.6 V1 Z" fill-rule="evenodd"/></svg></li>
        <li>info@seaward.example
          <svg viewBox="0 0 10 10"><path d="M0 2 H10 V8.5 H0 Z M0.5 2.4 L5 6 L9.5 2.4" /></svg></li>
        <li>www.seaward.example
          <svg viewBox="0 0 10 10"><circle cx="5" cy="5" r="4.6"/></svg></li>
      </ul>
      <p class="address">18, Harbour Road, Quayside<br>Aberdeen, AB11 5PQ</p>
    </div>
  </section>

  <section class="card card-back">
    <div class="brand">
      <span class="brand-dot"></span>
      <span class="brand-name">Seaward Delivery Group</span>
    </div>
  </section>
</div>
</body>
</html>
```